exclusive Speakeasy Bar Web design in New Jersey USA

We are opening a speakeasy in New Jersey USA soon. we are looking for a web designer to do our web site including the coding. we a looking for a 4 to 5 page web design. the site will be mostly static. home page, contact page, menu page and a link to a 3rd party site (most likely Quob) for reservations. we are looking for this designer to do our menu deign as well. we are looking for a quick turnaround 7-10 days. i am attaching some pictures for the designers to see the concept design and the actual current pictures with our logo as well. professionally taken pictures will be provided later on. our photographer will be taking the pictures in the next week.

Industry/Entity Type

Restaurant, Bar, Speakeasy

Coding

Coded - Design and coding required

Number of Pages Required

4 page

Requirements
Must have
• home page, contact page, menu page and a link to quob.com for reservations
Nice to have
• some videos

```html
<!DOCTYPE html>
<html lang="en">
<head>
<meta charset="utf-8">
<title>Velvet Room — Speakeasy Bar</title>
<link rel="stylesheet" href="https://fonts.googleapis.com/css2?family=Poppins:wght@400;500;600;700&family=Playfair+Display:wght@700;900&family=Roboto:wght@400;500&display=swap">
<style>
:root{
  --amber:#e5992b;
  --amber-strong:#e08a14;
  --rust:#c9650f;
  --ink:#141414;
  --night:#1c1c1d;
  --paper:#ffffff;
  --text:#2b2b2b;
}
*{margin:0;padding:0;box-sizing:border-box}
html,body{width:1200px;height:4149px;overflow:hidden}
body{position:relative;background:var(--paper);font-family:"Poppins",sans-serif;color:var(--text)}
.icon{display:inline-block;vertical-align:middle}

/* top bar */
.topbar{position:absolute;left:0;top:0;width:1200px;height:43px;background:var(--amber);color:#fff;font-size:13px;font-weight:500}
.topbar span{position:absolute;top:13px;display:flex;align-items:center;gap:6px}

/* hero */
.hero{position:absolute;left:0;top:43px;width:1200px;height:585px;overflow:hidden}
.hero-photo{position:absolute;inset:0;background:radial-gradient(ellipse at 55% 45%,#5a4530 0%,#2e2a26 45%,#141414 100%)}
.hero-shade{position:absolute;inset:0;background:linear-gradient(90deg,rgba(0,0,0,.45),rgba(0,0,0,.1) 60%,rgba(0,0,0,.25))}
.brand-name{position:absolute;left:113px;top:40px;color:#fff;font-size:18px;font-weight:600;line-height:22px}
.nav a{position:absolute;top:22px;color:#fff;font-size:15px;font-weight:500;text-decoration:none}
.btn-reserve{position:absolute;left:939px;top:17px;width:147px;height:36px;background:var(--amber);color:#fff;font-size:13px;font-weight:600;display:flex;align-items:center;justify-content:center;gap:7px}
.hero-title{position:absolute;left:110px;top:138px;font-size:54px;font-weight:700;line-height:58px;color:#fff}
.hero-title .accent{color:var(--amber)}
.hero-lede{position:absolute;left:113px;top:265px;width:440px;font-size:15.5px;line-height:24px;color:#fff}
.btn{position:absolute;height:36px;display:flex;align-items:center;justify-content:center;gap:10px;font-size:10.5px;font-weight:600;text-decoration:underline;letter-spacing:.3px}
.btn-amber{background:var(--amber);color:#fff}
.btn-light{background:#fff;color:var(--ink)}
.btn-dark{background:var(--ink);color:#fff}
.arrow-circle{position:absolute;width:42px;height:42px;border:2px solid var(--amber);border-radius:50%;display:flex;align-items:center;justify-content:center}

.contact-card{position:absolute;left:733px;top:107px;width:354px;height:435px;background:var(--amber);border-radius:20px;color:#fff;text-align:center}
.contact-card h3{margin-top:28px;font-size:23px;font-weight:600}
.contact-card p{margin:10px auto 0;width:300px;font-size:10.5px;line-height:17px}
.field{position:absolute;background:#eeb45a;height:34px;border-radius:2px;font-size:9.5px;color:#fff;text-align:left;padding:11px 12px}
.submit{position:absolute;left:106px;top:370px;width:145px;height:35px;background:var(--ink);color:#fff;font-size:10.5px;font-weight:600;display:flex;align-items:center;justify-content:center;gap:8px}

/* welcome */
.welcome{position:absolute;left:0;top:628px;width:1200px;height:730px;background:#fff}
.wordmark{position:absolute;left:360px;top:90px;width:320px;text-align:center;color:var(--ink);font-weight:500;font-size:44px;line-height:1}
.frame{position:absolute;background:#fff;padding:9px;box-shadow:0 4px 14px rgba(0,0,0,.18)}
.frame div{width:100%;height:100%}
.welcome h2{position:absolute;left:660px;top:196px;font-family:"Playfair Display",serif;font-weight:900;font-size:48px;line-height:50px;color:var(--ink)}
.welcome h2 .accent{color:var(--rust)}
.welcome p{position:absolute;left:660px;width:370px;font-size:14.2px;line-height:22.5px;color:var(--text)}

/* menu */
.menu{position:absolute;left:0;top:1358px;width:1200px;height:854px;overflow:hidden}
.menu-photo{position:absolute;inset:0;background:linear-gradient(180deg,#141516 0%,#2b3131 35%,#3a3a34 60%,#282420 100%)}
.menu-shade{position:absolute;inset:0;background:rgba(0,0,0,.35)}
.section-title{position:absolute;left:0;width:1200px;text-align:center;font-family:"Playfair Display",serif;font-weight:900;font-size:42px}
.section-sub{position:absolute;left:370px;width:460px;text-align:center;font-size:14px;line-height:19px}
.dish{position:absolute;width:420px;height:70px}
.dish .thumb{position:absolute;left:0;top:0;width:68px;height:68px;border-radius:50%;border:3px solid #fff;background:radial-gradient(circle at 40% 40%,#c6883c,#3a2616 75%)}
.dish h4{position:absolute;left:83px;top:-18px;font-size:16.5px;font-weight:600;color:var(--amber)}
.dish .desc{position:absolute;left:83px;top:4px;font-family:"Roboto",sans-serif;font-size:14px;color:#fff;white-space:nowrap}
.dish .price{position:absolute;left:85px;top:30px;width:66px;height:28px;background:var(--amber-strong);color:#fff;font-size:13px;font-weight:600;display:flex;align-items:center;justify-content:center}

/* location */
.location h2{position:absolute;left:110px;top:2397px;font-family:"Playfair Display",serif;font-weight:900;font-size:42px;color:var(--ink)}
.loc-item{position:absolute;left:113px;display:flex;align-items:center;gap:22px;font-family:"Roboto",sans-serif;font-size:15px;line-height:21px;color:var(--ink)}
.loc-icon{width:33px;height:33px;border-radius:50%;background:var(--amber-strong);display:flex;align-items:center;justify-content:center;flex:none}
.loc-photo{position:absolute;left:472px;top:2331px;width:615px;height:413px;background:linear-gradient(180deg,#2c3436 0%,#39494a 45%,#b9773a 75%,#7b5a3e 100%)}

/* news */
.news-card{position:absolute;top:2967px;width:308px}
.news-card .img{width:308px;height:257px}
.news-card .date{position:absolute;left:17px;top:-14px;width:96px;height:27px;background:var(--amber-strong);color:#fff;font-size:11.5px;display:flex;align-items:center;justify-content:center}
.news-card h4{margin-top:26px;font-size:16.5px;font-weight:600;color:var(--amber-strong)}
.news-card p{margin-top:6px;width:265px;font-family:"Roboto",sans-serif;font-size:13.5px;line-height:20px;color:#555}
.news-card .btn{position:relative;margin-top:16px;width:148px}

/* gallery */
.gallery{position:absolute;left:0;top:3477px;width:1200px;height:228px;display:flex}
.gallery div{flex:1;height:100%}

/* footer */
.footer{position:absolute;left:0;top:3705px;width:1200px;height:444px;background:var(--night);color:#fff}
.foot-brand{position:absolute;left:113px;top:100px;font-size:18px;font-weight:600;line-height:22px}
.foot-about{position:absolute;left:113px;top:170px;width:250px;font-size:13.5px;line-height:20px;color:#ddd}
.foot-book{position:absolute;left:113px;top:228px;font-size:11px;text-decoration:underline;color:#ddd}
.foot-phone{position:absolute;left:113px;top:242px;font-size:21px;font-weight:700;color:var(--amber-strong)}
.divider{position:absolute;top:65px;width:1px;height:250px;background:#3a3a3a}
.foot-col h5{position:absolute;top:68px;font-size:14px;font-weight:600;color:var(--amber-strong)}
.foot-col li{position:absolute;list-style:none;font-size:12px;color:#eee;display:flex;align-items:center;gap:7px}
.chev{color:var(--amber-strong);font-size:12px}
.sq{width:10px;height:10px;background:var(--amber-strong);display:inline-block}
.email-input{position:absolute;left:825px;top:103px;width:259px;height:34px;background:#fff;color:#333;font-size:11px;display:flex;align-items:center;gap:10px;padding-left:12px}
.subscribe{position:absolute;left:825px;top:148px;width:138px;height:34px;background:var(--amber-strong);color:#fff;font-size:10px;font-weight:600;text-decoration:underline;display:flex;align-items:center;justify-content:center;gap:8px}
.to-top{position:absolute;left:1039px;top:290px;width:44px;height:42px;background:var(--amber-strong);display:flex;align-items:center;justify-content:center}
.rule{position:absolute;left:113px;width:974px;height:1px;background:#3a3a3a}
.copyright{position:absolute;left:0;top:359px;width:1200px;text-align:center;font-size:12px;color:#ddd}
.copyright span{color:var(--amber-strong)}
</style>
</head>
<body>

<header class="topbar">
  <span style="left:113px"><svg class="icon" width="10" height="14" viewBox="0 0 10 14"><path d="M5 0a5 5 0 0 0-5 5c0 4 5 9 5 9s5-5 5-9a5 5 0 0 0-5-5zm0 7a2 2 0 1 1 0-4 2 2 0 0 1 0 4z" fill="#fff"/></svg>Quill Ln, Hoboken, NJ 07030, USA</span>
  <span style="left:749px"><svg class="icon" width="14" height="14" viewBox="0 0 14 14"><rect width="14" height="14" rx="3" fill="#fff"/><path d="M4 3l2 2-1 1.5c.7 1.3 1.6 2.2 2.5 2.5L9 8l2 2-1.3 1.3C7 11 3.3 7.5 3 4.3z" fill="#e5992b"/></svg>201-555-0148</span>
  <span style="left:903px"><svg class="icon" width="14" height="14" viewBox="0 0 14 14"><path d="M0 6L14 0 9 14 7 8z" fill="#fff"/></svg>booking@velvetroombar.com</span>
</header>

<section class="hero">
  <div class="hero-photo" role="img" aria-label="Dim speakeasy lounge with amber velvet chairs and a long bar"></div>
  <div class="hero-shade"></div>
  <div class="brand-name">Velvet Room</div>
  <nav class="nav">
    <a style="left:620px">Home</a>
    <a style="left:720px">Menu</a>
    <a style="left:819px">Contact Us</a>
  </nav>
  <a class="btn-reserve">Reservations <svg width="14" height="14" viewBox="0 0 14 14"><rect width="14" height="14" rx="2" fill="#fff"/><path d="M3.5 7l2.5 2.5 4.5-5" stroke="#e5992b" stroke-width="2" fill="none"/></svg></a>

  <h1 class="hero-title"><span class="accent">Seasonal &amp; Delicious</span><br>Food Menus</h1>
  <p class="hero-lede">Enjoy an exceptional journey of taste.It's our job every day to make important aspect of the customer experience a little bit better</p>
  <a class="btn btn-amber" style="left:113px;top:384px;width:124px">VIEW MENUS <svg width="13" height="13" viewBox="0 0 14 14"><circle cx="7" cy="7" r="7" fill="#fff"/><path d="M3.8 7l2.2 2.2 4.2-4.4" stroke="#e5992b" stroke-width="2" fill="none"/></svg></a>
  <a class="btn btn-light" style="left:271px;top:384px;width:146px">BOOK A TABLE <svg width="13" height="13" viewBox="0 0 14 14"><circle cx="7" cy="7" r="7" fill="#141414"/><path d="M3.8 7l2.2 2.2 4.2-4.4" stroke="#fff" stroke-width="2" fill="none"/></svg></a>

  <div class="arrow-circle" style="left:31px;top:279px"><svg width="12" height="14" viewBox="0 0 12 14"><path d="M8 2L3 7l5 5" stroke="#e5992b" stroke-width="2" fill="none"/></svg></div>
  <div class="arrow-circle" style="left:1124px;top:279px"><svg width="12" height="14" viewBox="0 0 12 14"><path d="M4 2l5 5-5 5" stroke="#e5992b" stroke-width="2" fill="none"/></svg></div>

  <form class="contact-card">
    <h3>Get In Touch</h3>
    <p>Printing and typesetting industry. Lorem Ipsum has been the industry's standard dummy</p>
    <div class="field" style="left:27px;top:124px;width:146px">Full Name:</div>
    <div class="field" style="left:188px;top:124px;width:146px">Email :</div>
    <div class="field" style="left:27px;top:172px;width:146px">Phone :</div>
    <div class="field" style="left:188px;top:172px;width:146px">Drinks<svg style="position:absolute;right:10px;top:13px" width="9" height="6" viewBox="0 0 9 6"><path d="M1 1l3.5 3.5L8 1" stroke="#fff" stroke-width="1.4" fill="none"/></svg></div>
    <div class="field" style="left:27px;top:220px;width:307px;height:126px">Comments :</div>
    <div class="submit">Submit Now <svg width="11" height="10" viewBox="0 0 11 10"><path d="M0 5h9M6 1.5L9.5 5 6 8.5" stroke="#fff" stroke-width="1.8" fill="none"/></svg></div>
  </form>
</section>

<section class="welcome">
  <div class="wordmark">Velvet Room</div>
  <div class="frame" style="left:113px;top:150px;width:227px;height:398px"><div role="img" aria-label="Bar counter with teal tiled front and industrial ceiling" style="background:linear-gradient(180deg,#2a2a2a 0%,#4a4a48 45%,#c79b8a 70%,#1f5a5a 100%)"></div></div>
  <div class="frame" style="left:279px;top:237px;width:314px;height:408px"><div role="img" aria-label="Shelves stocked with spirit bottles" style="background:linear-gradient(180deg,#3a2c20 0%,#8a6a48 30%,#d8cfc0 60%,#3b2f27 100%)"></div></div>
  <h2><span class="accent">Welcome</span> to<br>Velvet Room</h2>
  <p style="top:316px">When an unknown printer took a galley of type and scrambled it to make a type specimen book. It has survived not only five centuries, but also the leap into electronic</p>
  <p style="top:433px">pesetting, remaining essentially unchanged. It was popularised in the 1960s with the When an unknown printer took a galley of type and scrambled it to make a type specimen book.</p>
  <a class="btn btn-dark" style="left:660px;top:564px;width:146px">VIEW ALL MENU <svg width="13" height="13" viewBox="0 0 14 14"><circle cx="7" cy="7" r="7" fill="#fff"/><path d="M3.8 7l2.2 2.2 4.2-4.4" stroke="#141414" stroke-width="2" fill="none"/></svg></a>
</section>

<section class="menu">
  <div class="menu-photo" role="img" aria-label="Lounge interior with curved booths and back bar"></div>
  <div class="menu-shade"></div>
  <h2 class="section-title" style="top:80px;color:#fff">Menu</h2>
  <p class="section-sub" style="top:136px;color:#fff">It's the story of an everlasting love affair, Marco Verano and the Atlantic Ocean in the big air.</p>

  <div class="dish" style="left:171px;top:246px"><div class="thumb" role="img" aria-label="Cocktail"></div><h4>Chicha Morada</h4><p class="desc">Beetroot And Datterini, Goat Cheese, Ricotta</p><div class="price">$33.00</div></div>
  <div class="dish" style="left:670px;top:246px"><div class="thumb" role="img" aria-label="Cocktail"></div><h4>Chicha Morada</h4><p class="desc">Beetroot And Datterini, Goat Cheese, Ricotta</p><div class="price">$33.00</div></div>
  <div class="dish" style="left:171px;top:361px"><div class="thumb" role="img" aria-label="Cocktail"></div><h4>Chicha Morada</h4><p class="desc">Beetroot And Datterini, Goat Cheese, Ricotta</p><div class="price">$33.00</div></div>
  <div class="dish" style="left:670px;top:361px"><div class="thumb" role="img" aria-label="Cocktail"></div><h4>Chicha Morada</h4><p class="desc">Beetroot And Datterini, Goat Cheese, Ricotta</p><div class="price">$33.00</div></div>
  <div class="dish" style="left:171px;top:465px"><div class="thumb" role="img" aria-label="Cocktail" style="background:radial-gradient(circle at 45% 40%,#f1ede4,#5a5550 75%)"></div><h4>Chicha Morada</h4><p class="desc">Beetroot And Datterini, Goat Cheese, Ricotta</p><div class="price">$33.00</div></div>
  <div class="dish" style="left:670px;top:465px"><div class="thumb" role="img" aria-label="Cocktail"></div><h4>Chicha Morada</h4><p class="desc">Beetroot And Datterini, Goat Cheese, Ricotta</p><div class="price">$33.00</div></div>
  <div class="dish" style="left:171px;top:581px"><div class="thumb" role="img" aria-label="Cocktail"></div><h4>Chicha Morada</h4><p class="desc">Beetroot And Datterini, Goat Cheese, Ricotta</p><div class="price">$33.00</div></div>
  <div class="dish" style="left:670px;top:581px"><div class="thumb" role="img" aria-label="Cocktail"></div><h4>Chicha Morada</h4><p class="desc">Beetroot And Datterini, Goat Cheese, Ricotta</p><div class="price">$33.00</div></div>

  <a class="btn btn-amber" style="left:541px;top:746px;width:147px">VIEW ALL MENU <svg width="13" height="13" viewBox="0 0 14 14"><circle cx="7" cy="7" r="7" fill="#fff"/><path d="M3.8 7l2.2 2.2 4.2-4.4" stroke="#e5992b" stroke-width="2" fill="none"/></svg></a>
</section>

<section class="location">
  <h2>Find Location</h2>
  <div class="loc-item" style="top:2498px"><span class="loc-icon"><svg width="12" height="16" viewBox="0 0 10 14"><path d="M5 0a5 5 0 0 0-5 5c0 4 5 9 5 9s5-5 5-9a5 5 0 0 0-5-5zm0 7a2 2 0 1 1 0-4 2 2 0 0 1 0 4z" fill="#fff"/></svg></span><span>22/C, Elm Ave 1000 Jersey City<br>201 555 0190</span></div>
  <div class="loc-item" style="top:2571px"><span class="loc-icon"><svg width="15" height="11" viewBox="0 0 15 11"><rect x=".5" y=".5" width="14" height="10" fill="#fff"/><path d="M1 1l6.5 5L14 1" stroke="#e08a14" fill="none"/></svg></span><span>hello@velvetroombar.com</span></div>
  <div class="loc-item" style="top:2650px"><span class="loc-icon"><svg width="17" height="17" viewBox="0 0 17 17"><circle cx="8.5" cy="8.5" r="7" fill="none" stroke="#fff" stroke-width="2"/><path d="M8.5 4.5v4l3 2" stroke="#fff" stroke-width="1.8" fill="none"/></svg></span><span>Mon - Thu: 10 AM - 02 AM<br>Fri - Sun: 10 AM - 02 AM</span></div>
  <div class="loc-photo" role="img" aria-label="Bar room with teal walls, globe pendant lights and amber armchairs"></div>
</section>

<section class="news">
  <h2 class="section-title" style="top:2818px;color:#141414">Latest News</h2>
  <p class="section-sub" style="top:2878px;color:#2b2b2b">It's the story of an everlasting love affair, Marco Verano and the Atlantic Ocean in the big air.</p>

  <article class="news-card" style="left:113px"><div class="img" role="img" aria-label="Cocktails on a bar with bokeh lights" style="background:linear-gradient(160deg,#3b2e5a,#a0583c 55%,#2a1a12)"></div><span class="date">March 2,2023</span><h4>The story of an everlasting love</h4><p>The story of an everlasting love affair, Marco Verano and the Atlantic Ocean in the big air.</p><a class="btn btn-amber">READ MORE <svg width="13" height="13" viewBox="0 0 14 14"><circle cx="7" cy="7" r="7" fill="#fff"/><path d="M3.8 7l2.2 2.2 4.2-4.4" stroke="#e5992b" stroke-width="2" fill="none"/></svg></a></article>
  <article class="news-card" style="left:448px"><div class="img" role="img" aria-label="Bartender pouring a drink into a glass" style="background:linear-gradient(160deg,#1a1512,#6a3d1e 55%,#140f0c)"></div><span class="date">March 2,2023</span><h4>The story of an everlasting love</h4><p>The story of an everlasting love affair, Marco Verano and the Atlantic Ocean in the big air.</p><a class="btn btn-amber">READ MORE <svg width="13" height="13" viewBox="0 0 14 14"><circle cx="7" cy="7" r="7" fill="#fff"/><path d="M3.8 7l2.2 2.2 4.2-4.4" stroke="#e5992b" stroke-width="2" fill="none"/></svg></a></article>
  <article class="news-card" style="left:778px"><div class="img" role="img" aria-label="Whiskey poured over ice against city lights" style="background:linear-gradient(160deg,#1e2450,#4a3a7a 45%,#c68a3a 75%,#3a2812)"></div><span class="date">March 2,2023</span><h4>The story of an everlasting love</h4><p>The story of an everlasting love affair, Marco Verano and the Atlantic Ocean in the big air.</p><a class="btn btn-amber">READ MORE <svg width="13" height="13" viewBox="0 0 14 14"><circle cx="7" cy="7" r="7" fill="#fff"/><path d="M3.8 7l2.2 2.2 4.2-4.4" stroke="#e5992b" stroke-width="2" fill="none"/></svg></a></article>
</section>

<section class="gallery">
  <div role="img" aria-label="Back bar shelves of bottles" style="background:linear-gradient(180deg,#3a2a1e,#7a5a3a 50%,#2a1e16)"></div>
  <div role="img" aria-label="Painted wall mural with brass sconce" style="background:linear-gradient(180deg,#4a4e44,#6a6a58 50%,#3a3a30)"></div>
  <div role="img" aria-label="Bar counter under construction" style="background:linear-gradient(180deg,#2a2e30,#4a5a5c 50%,#2a3c3c)"></div>
  <div role="img" aria-label="Lounge seating with amber chairs" style="background:linear-gradient(180deg,#2a2c2e,#5a4a3a 50%,#b07a3a)"></div>
  <div role="img" aria-label="Liquor bottles on shelves" style="background:linear-gradient(180deg,#3a2a1c,#c8b8a0 50%,#2e241c)"></div>
</section>

<footer class="footer">
  <div class="foot-brand">Velvet Room</div>
  <p class="foot-about">The story of an everlasting love affair, Marco Verano and the Atlantic</p>
  <a class="foot-book">BOOK A TABLE</a>
  <p class="foot-phone">201 555 0177</p>

  <span class="divider" style="left:377px"></span>
  <span class="divider" style="left:557px"></span>
  <span class="divider" style="left:778px"></span>

  <div class="foot-col">
    <h5 style="left:417px">PAGES</h5>
    <ul>
      <li style="left:419px;top:96px"><span class="chev">›</span>Home</li>
      <li style="left:419px;top:129px"><span class="chev">›</span>Menu</li>
      <li style="left:419px;top:162px"><span class="chev">›</span>News</li>
      <li style="left:419px;top:195px"><span class="chev">›</span>Gallery</li>
      <li style="left:419px;top:228px"><span class="chev">›</span>Contact Us</li>
    </ul>
  </div>
  <div class="foot-col">
    <h5 style="left:609px">FOLLOW US ON</h5>
    <ul>
      <li style="left:611px;top:96px"><span class="sq"></span>Photos</li>
      <li style="left:611px;top:129px"><span class="sq"></span>Updates</li>
      <li style="left:611px;top:162px"><span class="sq"></span>Events</li>
      <li style="left:611px;top:195px"><span class="sq"></span>Videos</li>
    </ul>
  </div>
  <div class="foot-col">
    <h5 style="left:825px">NEWSLETTER SUBSCRIBE</h5>
  </div>
  <div class="email-input"><svg width="14" height="10" viewBox="0 0 15 11"><rect x=".5" y=".5" width="14" height="10" fill="#ccc"/><path d="M1 1l6.5 5L14 1" stroke="#fff" fill="none"/></svg>ENTER YOUR EMAIL ID :</div>
  <a class="subscribe">SUBSCRIBE NOW <svg width="12" height="12" viewBox="0 0 14 14"><circle cx="7" cy="7" r="7" fill="#fff"/><path d="M3.8 7l2.2 2.2 4.2-4.4" stroke="#e08a14" stroke-width="2" fill="none"/></svg></a>
  <a class="to-top"><svg width="14" height="9" viewBox="0 0 14 9"><path d="M1 8l6-6 6 6" stroke="#fff" stroke-width="2" fill="none"/></svg></a>

  <span class="rule" style="top:348px"></span>
  <p class="copyright">Copyright @2023 <span>Velvet Room</span></p>
  <span class="rule" style="top:388px"></span>
</footer>

</body>
</html>
```